Promotional Poster for Music Achievement Program

I need a vertical 11x17 poster designed for a new program called Bright Steps Music Achievement Program. The poster will be displayed in the lesson rooms and lobbies of music schools who use this program. The main headline of the flyer should be "Ask your teacher about Bright Steps" And then the additional text should be "Love your lessons and practice like never before with 10 levels of achievement!" I would like to use the logo on the flyer, which I uploaded here. In terms of artwork/design, I am looking for a fun, but clean feel. The purpose of the program is for students to progress through ten levels of achievement as they climb higher and higher to mastery of their instrument at level 10, so a feel of climbing, leveling up, or advancing would be good. And of course, this is a music program, so any musical artwork involved would make sense. But again - nothing too busy or overwhelming!

Target Market(s)

Parents waiting in the lobby of a music school.

Industry/Entity Type

Promotional

Colors

Designer to choose colors to be used in the design.

Requirements
Must have
• - Bright Steps logo
• - This headline: Ask your teacher about Bright Steps
• - This additional text: Love your lessons and practice like never before with 10 levels of achievement!
Nice to have
• In terms of artwork/design, I am looking for a fun, but clean feel. The purpose of the program is for students to progress through ten levels of achievement as they climb higher and higher to mastery of their instrument at level 10, so a feel of climbing, leveling up, or advancing would be good. And of course, this is a music program, so any musical artwork involved would make sense. But again - nothing too busy or overwhelming!
Should not have
• Should not be too busy.

```html
<!DOCTYPE html>
<html lang="en">
<head>
<meta charset="utf-8">
<title>Bright Steps Music Achievement Program – Poster</title>
<link rel="stylesheet" href="https://fonts.googleapis.com/css2?family=Exo+2:wght@600;700;800&display=swap">
<style>
  :root {
    --page-bg: #ecebe8;
    --poster-top: #e6e7eb;
    --poster-bottom: #d8dadf;
    --ink: #121212;
    --accent-red: #e1232b;
    --accent-green: #b3c91d;
    --shadow: rgba(0, 0, 0, 0.28);
  }
  html, body {
    margin: 0;
    width: 1200px;
    height: 1200px;
    overflow: hidden;
    background: var(--page-bg);
  }
  .poster {
    position: absolute;
    left: 189px;
    top: 20px;
    width: 822px;
    height: 1160px;
    background: linear-gradient(180deg, var(--poster-top), var(--poster-bottom));
    box-shadow: 0 4px 18px rgba(0,0,0,0.12);
    overflow: hidden;
    font-family: "Exo 2", "Trebuchet MS", sans-serif;
  }
  .music-artwork {
    position: absolute;
    inset: 0;
  }
  .brand {
    position: absolute;
    left: 81px;
    top: 70px;
    display: flex;
    align-items: center;
    gap: 14px;
    font-weight: 700;
    font-size: 40px;
    line-height: 1;
    color: var(--ink);
  }
  .brand-mark {
    width: 32px;
    height: 32px;
    background: var(--ink);
  }
  .headline {
    position: absolute;
    left: 74px;
    top: 190px;
    margin: 0;
    font-weight: 700;
    font-size: 142px;
    line-height: 170px;
    letter-spacing: -1px;
    color: var(--ink);
    text-shadow: 6px 8px 10px var(--shadow);
  }
  .headline span { display: block; white-space: nowrap; }
  .headline .highlight-red { color: var(--accent-red); }
  .headline .program-name {
    color: var(--accent-green);
    font-size: 112px;
  }
  .tagline {
    position: absolute;
    left: 82px;
    top: 955px;
    margin: 0;
    font-weight: 600;
    font-size: 46px;
    line-height: 57px;
    color: var(--ink);
    white-space: nowrap;
  }
</style>
</head>
<body>
  <main class="poster">
    <svg class="music-artwork" width="822" height="1160" viewBox="0 0 822 1160"
         role="img" aria-label="Colourful paper-cut music notes and clefs arranged in a rising treble clef shape along the right side">
      <defs>
        <linearGradient id="clefTones" x1="0" y1="0" x2="0" y2="1">
          <stop offset="0" stop-color="#f0a040"/>
          <stop offset="0.3" stop-color="#4fb85a"/>
          <stop offset="0.6" stop-color="#3f7fd0"/>
          <stop offset="1" stop-color="#c84a8a"/>
        </linearGradient>
        <filter id="soften" x="-30%" y="-30%" width="160%" height="160%">
          <feGaussianBlur stdDeviation="28"/>
        </filter>
      </defs>
      <g filter="url(#soften)" opacity="0.35">
        <path d="M600 60 C720 120 700 280 620 380 C540 480 470 560 520 660 C570 760 720 700 720 820 C720 940 600 960 560 900 C520 840 640 820 620 960 L600 1060"
              fill="none" stroke="url(#clefTones)" stroke-width="110" stroke-linecap="round"/>
        <ellipse cx="70" cy="1040" rx="90" ry="80" fill="#f3d628"/>
        <ellipse cx="10" cy="480" rx="40" ry="70" fill="#f0a040"/>
      </g>
    </svg>

    <div class="brand">
      <span class="brand-mark"></span>
      <span class="brand-name">Bright Steps</span>
    </div>

    <h1 class="headline">
      <span>Ask your</span>
      <span class="highlight-red">teacher</span>
      <span>about</span>
      <span class="program-name">Bright Steps</span>
    </h1>

    <p class="tagline">Love your lessons<br>and practice like never before<br>with 10 levels of achievement!</p>
  </main>
</body>
</html>
```